Etiketten für Bio Seifen
Zielgruppe
Wir stellen hochwertig 'handgemachte' Bio-Seifen her. Die Zielgruppe ist von 3-99 Jahren und zusätzlich haben wir auch noch Seife für Hunde.
Der Firmenname ist 'Kestrima'
Aufgabenstellung
Das Etikett soll Bezug auf Natur, Bio, Nachhaltigkeit nehmen. Wir stellen uns 'weiche' Aquarellfarben vor...Seife: Lavendel, Calendular, 7 Kräuter etc.
Das Etikett soll auf eine Beutelschachtel. Die Schachtel hat eine Anmaße: Breite 55mm; Höhe 120mm; Tiefe 30mm
Das Etikett soll im vorderen- und hinteren Bereich zusammenhängend geklebt werden.
Das Etikett soll eine Abmaße von: Breite 51mm; Höhe 114mm haben (Vorderseite) Rückseite gleich.
Wir möchten die Produkte auch gerne nummerieren, d.h. jede Seife hat eine Nummer die nicht zu groß dargestellt werden soll aber trotzdem gut leserlich.
Wir haben noch ein paar Bilder hochgeladen wie wir uns das ungefähr vorstellen.

```html
<!DOCTYPE html>
<html lang="de">
<head>
<meta charset="utf-8">
<title>Kestrima – Etiketten Bioseife</title>
<link href="https://fonts.googleapis.com/css2?family=Playfair+Display:ital,wght@0,400;1,400;1,700&family=Montserrat:wght@400&family=Sacramento&display=swap" rel="stylesheet">
<style>
  :root{
    --navy:#0b3d70;
    --frame:#c8c8c8;
    --paper:#ffffff;
    --lavender:#a9a3cc;
    --lavender-dark:#7c5aa6;
    --lavender-light:#e4e0f0;
    --calendula:#f2a322;
    --calendula-dark:#e88a1c;
    --calendula-light:#fbe3b6;
    --herb:#5db882;
    --herb-dark:#2f9a5a;
    --herb-light:#e2f1e6;
  }
  *{box-sizing:border-box;margin:0;padding:0}
  html,body{width:1200px;height:779px;overflow:hidden;background:var(--paper)}
  .sheet{position:relative;width:1200px;height:779px}
  .label{position:absolute;top:22px;width:336px;height:732px;border:1px solid var(--frame);background:var(--paper)}
  .label--lavender{left:22px;--accent:var(--lavender);--wash-a:var(--lavender-dark);--wash-b:var(--lavender-light)}
  .label--calendula{left:431px;--accent:var(--calendula);--wash-a:var(--calendula-dark);--wash-b:var(--calendula-light)}
  .label--herb{left:839px;--accent:var(--herb);--wash-a:var(--herb-dark);--wash-b:var(--herb-light)}
  .brand-name{position:absolute;left:0;width:336px;top:104px;text-align:center;
    font-family:'Playfair Display',serif;font-size:46px;color:var(--navy);letter-spacing:1px;line-height:1}
  .tagline{position:absolute;left:0;width:336px;top:176px;text-align:center;
    font-family:'Playfair Display',serif;font-style:italic;font-size:15px;color:var(--navy)}
  .category{position:absolute;left:55px;top:235px;width:226px;height:30px;background:var(--accent);
    font-family:'Montserrat',sans-serif;font-size:12.5px;letter-spacing:.6px;color:var(--navy);
    display:flex;align-items:center;justify-content:center}
  .artwork{position:absolute;left:15px;top:304px;width:306px;height:349px;
    background:radial-gradient(ellipse at 20% 30%,var(--wash-a) 0%,transparent 60%),
               linear-gradient(135deg,var(--wash-a) 0%,var(--accent) 45%,var(--wash-b) 100%)}
  .product-box{position:absolute;left:55px;top:552px;width:226px;height:77px;background:var(--accent);
    border:2px solid var(--navy);outline:1px solid var(--navy);outline-offset:-6px;
    text-align:center;color:var(--navy)}
  .product-number{font-family:'Montserrat',sans-serif;font-size:16px;margin-top:14px;line-height:1}
  .product-name{font-family:'Playfair Display',serif;font-style:italic;font-weight:700;font-size:21px;letter-spacing:1px;margin-top:6px;line-height:1}
  .benefit{position:absolute;left:15px;top:653px;width:306px;height:48px;background:var(--navy);
    color:#fff;font-family:'Sacramento',cursive;font-size:25px;display:flex;align-items:center;justify-content:center}
</style>
</head>
<body>
<main class="sheet">

  <section class="label label--lavender">
    <div class="brand-name">Kestrima</div>
    <p class="tagline">Natur auf der Haut</p>
    <div class="category">HANDGEMACHTE BIOSEIFE</div>
    <div class="artwork" role="img" aria-label="Aquarellfläche in Violett mit weiß gezeichneten Blüten"></div>
    <div class="product-box">
      <p class="product-number">N°1</p>
      <p class="product-name">LAVENDEL</p>
    </div>
    <p class="benefit">beruhigend &amp; entspannend</p>
  </section>

  <section class="label label--calendula">
    <div class="brand-name">Kestrima</div>
    <p class="tagline">Natur auf der Haut</p>
    <div class="category">HANDGEMACHTE BIOSEIFE</div>
    <div class="artwork" role="img" aria-label="Aquarellfläche in Orange und Gelb mit weiß gezeichneten Blüten"></div>
    <div class="product-box">
      <p class="product-number">N°2</p>
      <p class="product-name">CALENDULA</p>
    </div>
    <p class="benefit">mild reinigend &amp; sanft pflegend</p>
  </section>

  <section class="label label--herb">
    <div class="brand-name">Kestrima</div>
    <p class="tagline">Natur auf der Haut</p>
    <div class="category">HANDGEMACHTE BIOSEIFE</div>
    <div class="artwork" role="img" aria-label="Aquarellfläche in Grün mit weiß gezeichneten Blüten"></div>
    <div class="product-box">
      <p class="product-number">N°3</p>
      <p class="product-name">7 KRÄUTER</p>
    </div>
    <p class="benefit">nährend &amp; beruhigend</p>
  </section>

</main>
</body>
</html>
```